Brantley & Co Flyer (tri-fold) Accounting Firm

We are an accounting firm that provides loan broking services. We would like the brochure to look sophisticated but not too formal.

We would like to add some background colour to the flyer/brochure (attached in word and PDF version) in the following green (Hex Colour #94c947) in different styles/patterns etc.

Guidelines:

• We envisage that the green would cover approximately 30% of the background

• Do not change any of the content

• Change fonts as required

• The wording, titles/headings and background can be a combination of the green colour #94c947, black and white.

• We are happy to use multiple shadings of the green colour above to give contrast and depth

• We would like a 3-5mm bleed around the edges.

• Please remove black page break lines are to disappear (not sure how to remove on word document).

• Please stretch all images to the edge of the bleed (except for KLVN, Ledgerline Planner, Homeward Select and EasyNest 480 logos).

• Please insert different icons for phone, fax and email, e.g. an image of a telephone next to our number instead of the symbol “P”.

We have included a copy of a business card as an example of our existing style we wish to retain in the brochure.

Please provide appropriate file types to enable publishing of brochures.

Target Market(s)

Business owners and individuals requiring accounting and services, people requiring loans/refinance, superannuation retirees

Industry/Entity Type

Accounting

Font styles to use
Other font styles liked:
• Refer to business card font

Colors
abd037

Requirements
Must have
• Must use our Brantley & Co logo green with black text (as in the attached brochure).
Nice to have
• The design concept does not need to necessarily include the KLVN, Ledgerline Planner, Homeward Select and EasyNest 480 logos, this may create a simpler cleaner look. I'd like to look at the brochure design with and without those additional logos for comparison purposes.

```html
<!DOCTYPE html>
<html lang="en">
<head>
<meta charset="utf-8">
<title>Brantley &amp; Co – Tri-fold Brochure</title>
<link href="https://fonts.googleapis.com/css2?family=Arimo:wght@400;700&family=Montserrat:wght@500;600&display=swap" rel="stylesheet">
<style>
  :root{
    --green:#94c947;
    --green-mid:#76a833;
    --green-deep:#5d8f26;
    --green-dark:#4a7c1c;
    --heading-green:#2f4d14;
    --tick-green:#5f9a2a;
    --ink:#111;
    --ink-soft:#333;
    --white:#fff;
    --paper:#f3f4ef;
    --badge:#6b2a8f;
  }
  *{margin:0;padding:0;box-sizing:border-box}
  html,body{width:1200px;height:927px;overflow:hidden}
  body{background:radial-gradient(ellipse at 50% 45%,#ffffff 0%,var(--paper) 70%,#e9ebe4 100%);font-family:"Arimo",Arial,sans-serif;color:var(--ink);position:relative}
  .heading{font-family:"Montserrat",Helvetica,sans-serif;font-weight:500;font-size:27px;line-height:33px;color:var(--heading-green);position:absolute}
  .copy{position:absolute;font-size:17.6px;line-height:21.8px}
  .ticks{position:absolute;list-style:none;font-size:17.6px;line-height:21.8px}
  .ticks li{position:relative}
  .ticks li::before{content:"";position:absolute;width:6px;height:11px;border-right:2px solid var(--tick-green);border-bottom:2px solid var(--tick-green);transform:rotate(40deg);top:2px}
  .ticks.on-green li::before{border-color:var(--white)}

  /* left fold */
  .tax-panel{position:absolute;left:22px;top:0;width:359px;height:450px;background:linear-gradient(180deg,#7aac33,#72a42e);border-radius:0 0 10px 10px}
  .tax-panel .copy,.tax-panel .ticks{color:var(--white)}
  .tax-intro{left:22px;top:101px;width:300px}
  .tax-entities{left:75px;top:181px}
  .tax-entities li::before{left:-23px}
  .tax-including{left:45px;top:244px;color:var(--white)}
  .tax-list{left:76px;top:274px}
  .tax-list li::before{left:-23px}
  .business-intro{left:41px;top:534px;width:318px}
  .business-list{left:94px;top:614px}
  .business-list li::before{left:-20px}

  /* middle fold */
  .loan-panel{position:absolute;left:421px;top:0;width:360px;height:360px}
  .loan-photo{position:absolute;left:428px;top:162px;width:346px;height:164px;border-radius:14px;background:linear-gradient(100deg,#3a4049 0%,#8a929c 45%,#c7ccd2 60%,#4c535c 100%)}
  .loan-intro{left:458px;top:385px;width:300px}
  .loan-list{left:458px;top:525px}
  .loan-list li::before{left:-20px}
  .loan-call{left:458px;top:690px;width:290px}

  /* right fold */
  .super-panel{position:absolute;left:804px;top:0;width:396px;height:814px}
  .super-title{position:absolute;left:804px;width:396px;top:28px;text-align:center;color:var(--white);font-family:"Montserrat",Helvetica,sans-serif;font-weight:500;font-size:27px;line-height:34px}
  .super-intro{left:834px;top:99px;width:333px;font-size:16px;line-height:20px;color:var(--white)}
  .super-intro span{display:block;text-align:justify;text-align-last:justify;white-space:nowrap}
  .super-intro span.end{text-align-last:left}
  .super-list{left:858px;top:614px;color:var(--white)}
  .super-list li::before{left:-20px}
  .super-speak{left:858px;top:737px;width:265px;color:var(--white)}

  /* partner names */
  .partner{position:absolute;font-family:"Arimo",Arial,sans-serif;font-weight:400;font-size:18px;line-height:22px;color:var(--ink-soft)}
  .partner-badge{position:absolute;left:44px;top:856px;width:144px;height:50px;background:var(--badge);border-radius:3px}
  .partner-ledger{left:232px;top:869px}
  .partner-homeward{left:506px;top:869px}
  .partner-easynest{left:950px;top:879px}
</style>
</head>
<body>

<!-- left fold: tax and business -->
<div class="tax-panel">
  <h2 class="heading" style="left:25px;top:66px">Tax Services</h2>
  <p class="copy tax-intro">We prepare tax returns ranging from the simplest individual return to the most complex business.</p>
  <ul class="ticks on-green tax-entities">
    <li>Individuals, partnerships,<br>companies, trusts and SMSF’s</li>
  </ul>
  <p class="copy tax-including">Including:</p>
  <ul class="ticks on-green tax-list">
    <li>Rental properties</li>
    <li>Capital Gains Tax</li>
    <li>Share Portfolios</li>
    <li>GST, BAS and IAS</li>
    <li>Deceased estates</li>
    <li>Tax Planning</li>
    <li>ATO communications</li>
  </ul>
</div>

<h2 class="heading" style="left:42px;top:477px">Own your own business?</h2>
<p class="copy business-intro">We understand running a business is hard work. Let us work with you to help improve your business performance.</p>
<ul class="ticks business-list">
  <li>New business start up</li>
  <li>Purchase and sale of business</li>
  <li>Asset protection</li>
  <li>Succession planning</li>
  <li>Purchase and sale of property</li>
  <li>Budgeting and benchmarking</li>
  <li>Cloud accounting software</li>
</ul>

<!-- middle fold: loans -->
<svg class="loan-panel" viewBox="0 0 360 360" aria-hidden="true">
  <defs>
    <linearGradient id="loanGreen" x1="0" y1="0" x2="0" y2="1">
      <stop offset="0" stop-color="#7aac33"/><stop offset="1" stop-color="#6e9f2c"/>
    </linearGradient>
  </defs>
  <path d="M0 0H360V322Q360 332 350 333Q250 356 180 358Q110 356 10 333Q0 332 0 322Z" fill="url(#loanGreen)"/>
</svg>
<h2 class="heading" style="left:421px;width:360px;top:66px;text-align:center">Have you reviewed your<br>loan lately?</h2>
<div class="loan-photo" role="img" aria-label="Photo: businessman pressing a touchscreen button labelled Mortgage, with Interest below"></div>

<p class="copy loan-intro">We provide our clients with a FREE annual review of their existing commercial and residential loan portfolio and can assist our clients in obtaining new loans.</p>
<ul class="ticks loan-list">
  <li>Free annual loan portfolio review</li>
  <li>Selection of 25 residential lenders</li>
  <li>Selection of 8 commercial lenders</li>
  <li>Secure competitive rates<br>available in the market</li>
</ul>
<p class="copy loan-call">Simply give us a call and we will handle the rest.</p>

<!-- right fold: super -->
<svg class="super-panel" viewBox="0 0 396 814" aria-hidden="true">
  <defs>
    <linearGradient id="superGreen" x1="0" y1="0" x2="1" y2="1">
      <stop offset="0" stop-color="#4a7c1c"/><stop offset="0.5" stop-color="#5d8f26"/><stop offset="1" stop-color="#76a833"/>
    </linearGradient>
    <linearGradient id="superPhoto" x1="0" y1="0" x2="1" y2="0">
      <stop offset="0" stop-color="#5a4a3c"/><stop offset="0.45" stop-color="#7d7064"/><stop offset="0.75" stop-color="#c9c3ba"/><stop offset="1" stop-color="#9aa2ab"/>
    </linearGradient>
  </defs>
  <path d="M0 0H396V744Q220 800 0 814Z" fill="url(#superGreen)"/>
  <path d="M0 300Q180 250 396 298V496Q240 570 0 588Z" fill="url(#superPhoto)" role="img" aria-label="Photo: smiling mature man with folded arms in a bookshop"/>
</svg>
<h2 class="super-title">Take control of your<br>Super</h2>
<p class="copy super-intro">
  <span>SMSF's are a fast growing vehicle for</span>
  <span>investment, accounting for approximately one</span>
  <span>third of all superannuation assets with more</span>
  <span class="end">than 6,500 funds being setup per quarter.</span>
  <span>The SMSF structure enables members to</span>
  <span>have the flexibility to CONTROL their</span>
  <span>investment strategy to suit their personal</span>
  <span class="end">circumstances.</span>
</p>
<ul class="ticks on-green super-list">
  <li>SMSF Establishment/Rollover</li>
  <li>Compliance obligations</li>
  <li>Consultancy and strategic advice</li>
  <li>Retirement strategies</li>
  <li>Estate planning</li>
</ul>
<p class="copy super-speak">Speak to one of our consultants about our SMSF services.</p>

<!-- partners -->
<div class="partner-badge" role="img" aria-label="Certified consultant badge"></div>
<span class="partner partner-ledger">Ledgerline Planner</span>
<span class="partner partner-homeward">Homeward Select</span>
<span class="partner partner-easynest">EasyNest 480</span>

</body>
</html>
```